Business Card Design for Event Planning Company

Create a business card for event planning company using our new logo. After I pick the design, I will need files made for 6 employees. Our company provides event design & logistics services as well as venue management. The font should be sans serif and complementary to the logo. I will need to know the name of the font selected for the final design. The phone numbers listed should be separated by "." not "-"

Address for the card
PO Box 318, Washington, DC 20019

Card One
Lorna Pettibone
lpettibone@galavoyant.com
202.481.7730

Card Two
Miriam Okonkwo
mokonkwo@galavoyant.com
202.556.2047

Card Three
Tessa Varnholt
tvarnholt@galavoyant.com
978.620.4471

Card Four
Robin Fess
rfess@galavoyant.com
202.718.3362

Card Five
Ada-Rose Pelletan-Uzor
adarose@galavoyant.com
202.839.1205

Card Six
Beatrix Holloway
Beatrix@galavoyant.com
202.492.6618

Target Market(s)

Corporate/Non-Profit

Industry/Entity Type

Event Planning

Contact Information for Business Card

Address for the card

Card One
Lorna Pettibone
lpettibone@galavoyant.com
202.481.7730

Card Two
Miriam Okonkwo
202.556.2047

Card Three
Tessa Varnholt
978.620.4471

Card Four
Robin Fess
rfess@galavoyant.com
202.718.3362

Card Five
Ada-Rose Pelletan-Uzor
202.839.1205

Card Six
Beatrix Holloway
202.492.6618

Font styles to use
Sans Serif

Colors

Designer to choose colors to be used in the design.

Requirements
Must have
• Two-sided with logo
Should not have
• Extra colors or be too busy

```html
<!DOCTYPE html>
<html lang="en">
<head>
<meta charset="utf-8">
<title>Galavoyant Business Cards</title>
<link rel="stylesheet" href="https://fonts.googleapis.com/css2?family=Montserrat:wght@700&family=Questrial&display=swap">
<style>
  :root {
    --ink: #231a18;
    --teal: #6aa6a3;
    --paper: #ffffff;
    --rule: #b9b9b9;
    --mist: #d9eceb;
  }
  * { box-sizing: border-box; margin: 0; padding: 0; }
  html, body { width: 807px; height: 1200px; overflow: hidden; background: var(--paper); }
  body { position: relative; font-family: "Questrial", sans-serif; color: var(--ink); }

  .card { position: absolute; width: 287px; height: 158px; }
  .front { left: 106px; border-top-right-radius: 20px; overflow: hidden; display: flex; flex-direction: column; align-items: center; justify-content: center; }
  .front--dark { background: var(--ink); }
  .front--teal { background: var(--teal); }
  .front__texture { position: absolute; inset: 0; }
  .front--dark .front__texture { background: linear-gradient(135deg, #2b2120, #1e1615); }
  .front--teal .front__texture { background: linear-gradient(135deg, #70aba8, #64a09d); }
  .front__mark { position: relative; width: 20px; height: 20px; border-radius: 50%; margin-bottom: 6px; }
  .front--dark .front__mark { background: var(--teal); }
  .front--teal .front__mark { background: var(--paper); }
  .front__wordmark { position: relative; font-size: 25px; letter-spacing: 0.5px; line-height: 1; }
  .front--dark .front__wordmark { color: var(--teal); }
  .front--teal .front__wordmark { color: var(--ink); }
  .front__url { position: relative; font-size: 10px; margin-top: 7px; }
  .front--dark .front__url { color: var(--paper); }
  .front--teal .front__url { color: var(--mist); }

  .back { left: 415px; background: var(--paper); border: 1px solid var(--rule); border-bottom-right-radius: 20px; overflow: hidden; }
  .back__name { position: absolute; left: 29px; top: 34px; font-family: "Montserrat", sans-serif; font-weight: 700; font-size: 19px; line-height: 1; text-transform: uppercase; letter-spacing: 0.2px; }
  .back__name--stacked { top: 23px; font-size: 18px; line-height: 0.95; }
  .back__first { color: var(--teal); }
  .back__last { color: var(--ink); }
  .contacts { position: absolute; left: 29px; top: 74px; list-style: none; }
  .back__name--stacked + .contacts { top: 78px; }
  .contacts li { display: flex; align-items: center; gap: 5px; font-size: 8.6px; height: 16px; color: #3a3331; }
  .contacts svg { width: 7px; height: 7px; flex: none; }
  .brand { position: absolute; right: 18px; top: 66px; display: flex; align-items: center; gap: 5px; }
  .brand__dot { width: 16px; height: 16px; border-radius: 50%; background: var(--teal); }
  .brand__name { font-size: 15px; color: var(--ink); }
  .address { position: absolute; left: 40px; bottom: 0; width: 206px; height: 19px; border-radius: 8px 8px 0 0; font-size: 8.5px; color: var(--paper); display: flex; align-items: center; justify-content: center; }
  .address--dark { background: var(--ink); }
  .address--teal { background: var(--teal); }

  .row1 { top: 35px; } .row2 { top: 217px; } .row3 { top: 397px; }
  .row4 { top: 579px; } .row5 { top: 760px; } .row6 { top: 942px; }
</style>
</head>
<body>
<svg width="0" height="0" style="position:absolute" aria-hidden="true">
  <symbol id="icon-phone" viewBox="0 0 8 8"><rect x="2" y="0.5" width="4" height="7" rx="0.8" fill="none" stroke="#8a8a8a" stroke-width="0.9"/></symbol>
  <symbol id="icon-mail" viewBox="0 0 8 8"><rect x="0.5" y="1.5" width="7" height="5" fill="#8a8a8a"/><path d="M0.5 1.5 L4 4.5 L7.5 1.5" fill="none" stroke="#fff" stroke-width="0.8"/></symbol>
  <symbol id="icon-web" viewBox="0 0 8 8"><circle cx="4" cy="4" r="3.5" fill="#8a8a8a"/><path d="M0.5 4 H7.5 M4 0.5 C2 2.5 2 5.5 4 7.5 M4 0.5 C6 2.5 6 5.5 4 7.5" fill="none" stroke="#fff" stroke-width="0.6"/></symbol>
</svg>

<!-- Card 1 -->
<section class="card front front--dark row1">
  <div class="front__texture" role="img" aria-label="Subtle interlocking leaf pattern in dark brown"></div>
  <span class="front__mark"></span><span class="front__wordmark">galavoyant</span><span class="front__url">www.galavoyant.com</span>
</section>
<section class="card back row1">
  <h2 class="back__name"><span class="back__first">Lorna</span> <span class="back__last">Pettibone</span></h2>
  <ul class="contacts">
    <li><svg><use href="#icon-phone"/></svg>202.481.7730</li>
    <li><svg><use href="#icon-mail"/></svg>lpettibone@galavoyant.com</li>
    <li><svg><use href="#icon-web"/></svg>www.galavoyant.com</li>
  </ul>
  <div class="brand"><span class="brand__dot"></span><span class="brand__name">galavoyant</span></div>
  <p class="address address--dark">PO Box 318, Washington, DC 20019</p>
</section>

<!-- Card 2 -->
<section class="card front front--teal row2">
  <div class="front__texture" role="img" aria-label="Subtle interlocking leaf pattern in teal"></div>
  <span class="front__mark"></span><span class="front__wordmark">galavoyant</span><span class="front__url">www.galavoyant.com</span>
</section>
<section class="card back row2">
  <h2 class="back__name"><span class="back__first">Miriam</span> <span class="back__last">Okonkwo</span></h2>
  <ul class="contacts">
    <li><svg><use href="#icon-phone"/></svg>202.556.2047</li>
    <li><svg><use href="#icon-mail"/></svg>mokonkwo@galavoyant.com</li>
    <li><svg><use href="#icon-web"/></svg>www.galavoyant.com</li>
  </ul>
  <div class="brand"><span class="brand__dot"></span><span class="brand__name">galavoyant</span></div>
  <p class="address address--teal">PO Box 318, Washington, DC 20019</p>
</section>

<!-- Card 3 -->
<section class="card front front--dark row3">
  <div class="front__texture" role="img" aria-label="Subtle interlocking leaf pattern in dark brown"></div>
  <span class="front__mark"></span><span class="front__wordmark">galavoyant</span><span class="front__url">www.galavoyant.com</span>
</section>
<section class="card back row3">
  <h2 class="back__name"><span class="back__first">Tessa</span> <span class="back__last">Varnholt</span></h2>
  <ul class="contacts">
    <li><svg><use href="#icon-phone"/></svg>978.620.4471</li>
    <li><svg><use href="#icon-mail"/></svg>tvarnholt@galavoyant.com</li>
    <li><svg><use href="#icon-web"/></svg>www.galavoyant.com</li>
  </ul>
  <div class="brand"><span class="brand__dot"></span><span class="brand__name">galavoyant</span></div>
  <p class="address address--dark">PO Box 318, Washington, DC 20019</p>
</section>

<!-- Card 4 -->
<section class="card front front--teal row4">
  <div class="front__texture" role="img" aria-label="Subtle interlocking leaf pattern in teal"></div>
  <span class="front__mark"></span><span class="front__wordmark">galavoyant</span><span class="front__url">www.galavoyant.com</span>
</section>
<section class="card back row4">
  <h2 class="back__name"><span class="back__first">Robin</span> <span class="back__last">Fess</span></h2>
  <ul class="contacts">
    <li><svg><use href="#icon-phone"/></svg>202.718.3362</li>
    <li><svg><use href="#icon-mail"/></svg>rfess@galavoyant.com</li>
    <li><svg><use href="#icon-web"/></svg>www.galavoyant.com</li>
  </ul>
  <div class="brand"><span class="brand__dot"></span><span class="brand__name">galavoyant</span></div>
  <p class="address address--teal">PO Box 318, Washington, DC 20019</p>
</section>

<!-- Card 5 -->
<section class="card front front--dark row5">
  <div class="front__texture" role="img" aria-label="Subtle interlocking leaf pattern in dark brown"></div>
  <span class="front__mark"></span><span class="front__wordmark">galavoyant</span><span class="front__url">www.galavoyant.com</span>
</section>
<section class="card back row5">
  <h2 class="back__name back__name--stacked"><span class="back__first">Ada-Rose</span><br><span class="back__last">Pelletan-Uzor</span></h2>
  <ul class="contacts">
    <li><svg><use href="#icon-phone"/></svg>202.839.1205</li>
    <li><svg><use href="#icon-mail"/></svg>adarose@galavoyant.com</li>
    <li><svg><use href="#icon-web"/></svg>www.galavoyant.com</li>
  </ul>
  <div class="brand"><span class="brand__dot"></span><span class="brand__name">galavoyant</span></div>
  <p class="address address--dark">PO Box 318, Washington, DC 20019</p>
</section>

<!-- Card 6 -->
<section class="card front front--teal row6">
  <div class="front__texture" role="img" aria-label="Subtle interlocking leaf pattern in teal"></div>
  <span class="front__mark"></span><span class="front__wordmark">galavoyant</span><span class="front__url">www.galavoyant.com</span>
</section>
<section class="card back row6">
  <h2 class="back__name back__name--stacked"><span class="back__first">Beatrix</span><br><span class="back__last">Holloway</span></h2>
  <ul class="contacts">
    <li><svg><use href="#icon-phone"/></svg>202.492.6618</li>
    <li><svg><use href="#icon-mail"/></svg>Beatrix@galavoyant.com</li>
    <li><svg><use href="#icon-web"/></svg>www.galavoyant.com</li>
  </ul>
  <div class="brand"><span class="brand__dot"></span><span class="brand__name">galavoyant</span></div>
  <p class="address address--teal">PO Box 318, Washington, DC 20019</p>
</section>
</body>
</html>
```